Our Pantry Remedy

I am a pharmacist turn chef and my current website www.ourpantryremedy.com is in desperate need of a make over. I want to be able to add how to videos, photographs and have tabs. The tabs needed will be Home, About, Recipes, Health & Wellness, Services, Confidentiality, Affordability, Blog, Articles and Friday Cocktails. Eventually I will want a news letter, but do not want that now, only the ability to add it later. I will also want to add a market place tab later to sell merchandise and ebooks. The ability to navigate should be easy and not confusing and the ability to post should be easy. I will need social media Friendloop, Clipquarry, zorvix plus, zorvix, Snapvale and blurtle. In addition I will need some direction on how to operate the site. Examples of website I like (but do not want to copy) are www.buildsoundvigor.net www.drmarkbrevoni.com. It is best for me to work with someone who can explain things simply.
Updates

Another website I think is nice is www.tqgalley.com  Thanks!

Target Market(s)

The business will be diving right into the delicious side of Key West’s good health as a personal chef, a culinary wellness coach, a wellness cooking teacher, a healthful caterer and a wellness host and entertainer.
The site needs to promote health with the art of food because I am convinced that health is best enhanced, maintained and recovered through nutritious eating and cuisine, and not through pills.
I will be infusing fresh recipes with a Key West flair in hopes to share my passion and insights into nutrition and health with residents and visitors alike. I want everyone to feel welcome to come in and join the fun.

Industry/Entity Type

Chef

Colors

Requirements
Must have
• Easy navigation, easy operation and posting and social media tools. Spam filters to keep the creeps away and important plugins that make it all work.
Nice to have
• Everything is nice to have

```html
<!DOCTYPE html>
<html lang="en">
<head>
<meta charset="utf-8">
<title>Chef Dale Marrow – Our Pantry Remedy</title>
<link href="https://fonts.googleapis.com/css2?family=Lato:ital,wght@0,400;0,700;1,400&family=Tinos:ital@0;1&display=swap" rel="stylesheet">
<style>
  :root {
    --ink: #333333;
    --ink-soft: #555555;
    --bar-dark: #111111;
    --bar-light: #f7f7f7;
    --band: #f6f6f6;
    --rule: #e4e4e4;
    --green: #6aaa2a;
    --brand-green: #1e8a3c;
    --orange: #f08a24;
    --coral: #ea5a3a;
    --bracket: #ef6a34;
    --icon-dark: #3c3c3c;
    --footer: #2a2a2a;
    --footer-text: #d6d6d6;
    --white: #ffffff;
  }
  * { box-sizing: border-box; margin: 0; padding: 0; }
  html, body { width: 1105px; height: 1200px; overflow: hidden; background: var(--white); }
  body { position: relative; font-family: "Lato", sans-serif; color: var(--ink); }
  .abs { position: absolute; }

  .top-bar { left: 0; top: 0; width: 1105px; height: 43px; background: var(--bar-dark); }
  .sub-bar { left: 0; top: 43px; width: 1105px; height: 35px; background: var(--bar-light); }

  .brand-box { left: 190px; top: 0; width: 168px; height: 88px; background: var(--white);
    border: 1px solid #dddddd; border-top: none; box-shadow: 0 3px 6px rgba(0,0,0,.08);
    display: flex; align-items: center; justify-content: center; gap: 7px; }
  .brand-mark { width: 10px; height: 10px; border-radius: 50%; background: var(--brand-green); }
  .brand-name { font-family: "Lato", sans-serif; font-size: 17px; color: var(--brand-green); font-weight: 400; }

  .main-nav { right: 189px; top: 0; height: 43px; display: flex; align-items: center; gap: 14px; list-style: none; }
  .main-nav li { font-size: 9px; color: var(--white); }
  .main-nav .is-current { color: var(--orange); font-weight: 700; }
  .util-nav { right: 189px; top: 43px; height: 35px; display: flex; align-items: center; gap: 12px; list-style: none; }
  .util-nav li { font-size: 8.5px; color: var(--ink); }

  .hero-title { left: 0; width: 1125px; top: 102px; text-align: center; font-family: "Tinos", serif;
    font-size: 24px; color: var(--green); }
  .hero-lead { left: 0; width: 1121px; top: 136px; text-align: center; font-family: "Tinos", serif;
    font-size: 13.5px; color: var(--ink); }
  .hero-lead em { color: var(--coral); }

  .guide-band { left: 0; top: 388px; width: 1105px; height: 312px; background: var(--band);
    border-top: 1px solid var(--rule); border-bottom: 1px solid var(--rule); }

  .hero-visual { left: 314px; top: 176px; width: 497px; height: 382px; border-radius: 10px;
    background: linear-gradient(180deg, #f4ece6 0%, #e9ded6 55%, #d9c8b8 100%);
    border: 20px solid #121212; }
  .hero-stand { left: 486px; top: 478px; width: 156px; height: 82px;
    background: linear-gradient(90deg, #b8b8b8, #efefef 50%, #b0b0b0);
    clip-path: polygon(18% 0, 82% 0, 90% 85%, 100% 100%, 0 100%, 10% 85%); }

  .section-title { left: 0; width: 1101px; top: 596px; text-align: center; font-size: 18.5px; font-weight: 700;
    color: var(--ink); }
  .section-copy { left: 290px; width: 520px; top: 629px; text-align: center; font-size: 8.6px; line-height: 13px; color: var(--ink-soft); }

  .feature { width: 170px; text-align: center; }
  .feature-icon { display: block; margin: 0 auto; }
  .feature-title { margin-top: 18px; font-size: 12px; font-weight: 700; line-height: 14.5px; color: var(--ink); height: 30px; }
  .feature.is-active .feature-title { color: var(--green); }
  .feature-copy { margin-top: 20px; font-size: 8.8px; line-height: 13.5px; color: var(--ink-soft); }
  .focus-frame { left: 234px; top: 718px; width: 158px; height: 128px; }

  .gallery-rule { left: 322px; top: 938px; width: 465px; height: 1px; background: var(--rule); }
  .gallery { left: 209px; top: 972px; display: flex; gap: 13px; }
  .gallery-item { width: 167px; height: 119px; border: 1px solid #dddddd; padding: 3px; background: var(--white); }
  .gallery-fill { width: 100%; height: 100%; }

  .site-footer { left: 0; top: 1122px; width: 1105px; height: 78px; background: var(--footer); }
  .footer-nav { left: 210px; top: 1145px; display: flex; gap: 14px; list-style: none; }
  .footer-nav li { font-size: 9px; color: var(--footer-text); }
  .footer-nav .is-current { color: var(--orange); font-weight: 700; }
  .footer-rule { left: 0; top: 1177px; width: 1105px; height: 1px; background: #3d3d3d; }
  .copyright { left: 211px; top: 1183px; font-size: 8.5px; color: #a9a9a9; }
  .follow-label { left: 800px; top: 1133px; font-family: "Tinos", serif; font-size: 11px; color: var(--white); }
  .social-list { left: 798px; top: 1150px; display: flex; gap: 4px; list-style: none; }
  .social-list li { width: 20px; height: 20px; border-radius: 50%; background: var(--white); }
</style>
</head>
<body>
  <header>
    <div class="abs top-bar"></div>
    <div class="abs sub-bar"></div>
    <div class="abs brand-box"><span class="brand-mark"></span><span class="brand-name">Chef Dale Marrow</span></div>
    <ul class="abs main-nav">
      <li class="is-current">Home</li><li>Recipes</li><li>Health &amp; Wellness</li><li>Services</li>
      <li>Confidentiality</li><li>Affordability</li><li>Friday Cocktails</li>
    </ul>
    <ul class="abs util-nav">
      <li>About</li><li>Contact</li><li>Blogs</li><li>Articles</li>
    </ul>
  </header>

  <main>
    <h1 class="abs hero-title">Fresh recipes with a Key West flair</h1>
    <p class="abs hero-lead">Proin gravida nibh vel velit auctor aliquet. <em>Aenean sollicitudin</em> lorem quis bibendum auctor, nisi elit consequat</p>

    <div class="abs guide-band"></div>
    <div class="abs hero-stand"></div>
    <div class="abs hero-visual" role="img" aria-label="Hero banner: smiling woman in yoga pose holding a salad plate and a dumbbell, with chef brand name and chicken wraps"></div>

    <h2 class="abs section-title">SELF AWARENESS AND PROPER GUIDANCE</h2>
    <p class="abs section-copy">This is Pixelforge's version of Lorem Ipsum. Proin gravida nibh vel velit auctor aliquet. Aenean sollicitudin, lorem quis bibendum auctor, nisi elit <em>consequat ipsum</em>, nec sagittis sem nibh id elit. Duis sed odio sit amet nibh vulputate cursus a sit amet mauris. Morbi accumsan ipsum velit. Nam nec tellus a odio tincidunt auctor a ornare odio.</p>

    <svg class="abs focus-frame" viewBox="0 0 158 128" aria-hidden="true">
      <g fill="none" stroke="var(--bracket)" stroke-width="2.5">
        <path d="M1 24V1H24M134 1H157V24M1 104V127H24M134 127H157V104"/>
      </g>
    </svg>

    <section class="abs feature is-active" style="left:228px;top:740px;">
      <svg class="feature-icon" width="44" height="40" viewBox="0 0 44 40" aria-hidden="true">
        <path d="M21 38 C8 28 2 21 2 13 C2 6 7 2 13 2 C17 2 20 4 21 7 C22 4 25 2 29 2 C35 2 40 6 40 13 C40 21 34 28 21 38Z" fill="var(--coral)"/>
        <circle cx="33" cy="27" r="9" fill="var(--coral)" stroke="var(--white)" stroke-width="2"/>
        <path d="M33 22V32M28 27H38" stroke="var(--white)" stroke-width="2.5"/>
      </svg>
      <h3 class="feature-title">HEALTHY LIVING AND<br>PROPER DIET</h3>
      <p class="feature-copy">This is Pixelforge's version of Lorem Ipsum. Proin gravida nibh vel velit auctor aliquet.</p>
    </section>

    <section class="abs feature" style="left:469px;top:740px;">
      <svg class="feature-icon" width="44" height="40" viewBox="0 0 44 40" aria-hidden="true">
        <path d="M16 6V2H28V6" fill="none" stroke="var(--icon-dark)" stroke-width="3"/>
        <rect x="2" y="7" width="40" height="31" rx="3" fill="var(--icon-dark)"/>
        <path d="M22 15V31M14 23H30" stroke="var(--white)" stroke-width="4"/>
      </svg>
      <h3 class="feature-title">HEALTH &amp; SAFETY<br>TOPICS</h3>
      <p class="feature-copy">This is Pixelforge's version of Lorem Ipsum. Proin gravida nibh vel velit auctor aliquet.</p>
    </section>

    <section class="abs feature" style="left:721px;top:740px;">
      <svg class="feature-icon" width="44" height="40" viewBox="0 0 44 40" aria-hidden="true">
        <g fill="var(--icon-dark)">
          <rect x="11" y="6" width="5" height="20" rx="2.5"/>
          <rect x="17" y="1" width="5" height="24" rx="2.5"/>
          <rect x="23" y="2" width="5" height="23" rx="2.5"/>
          <rect x="29" y="6" width="5" height="20" rx="2.5"/>
          <path d="M11 20H34V28C34 34 30 39 23 39H20C14 39 11 34 11 30Z"/>
          <path d="M11 26L4 17C3 15 6 13 8 15L14 22Z"/>
        </g>
      </svg>
      <h3 class="feature-title">ASK EXPERTS AND<br>EXPLORE MORE</h3>
      <p class="feature-copy">This is Pixelforge's version of Lorem Ipsum. Proin gravida nibh vel velit auctor aliquet.</p>
    </section>

    <div class="abs gallery-rule"></div>
    <div class="abs gallery">
      <div class="gallery-item"><div class="gallery-fill" role="img" aria-label="Grilled salmon with asparagus and lemon on a white plate" style="background:linear-gradient(135deg,#eef1ef,#e8945a 55%,#d9dfcf);"></div></div>
      <div class="gallery-item"><div class="gallery-fill" role="img" aria-label="Two hands cupped around a red heart" style="background:radial-gradient(circle at 50% 55%,#c8141c 0,#d23a3a 22%,#e9d7cc 45%,#f2f2f2 75%);"></div></div>
      <div class="gallery-item"><div class="gallery-fill" role="img" aria-label="Spoon of yogurt with berries and granola in front of oranges" style="background:linear-gradient(160deg,#f2c41c,#f49b1a 50%,#f6efe4);"></div></div>
      <div class="gallery-item"><div class="gallery-fill" role="img" aria-label="Bowl of spiced chickpea curry with lime on a dark table" style="background:radial-gradient(circle at 50% 55%,#b4622a 0,#8a4a22 30%,#3a2a1e 70%,#1e1a16);"></div></div>
    </div>
  </main>

  <footer>
    <div class="abs site-footer"></div>
    <ul class="abs footer-nav">
      <li class="is-current">Home</li><li>Recipes</li><li>Health &amp; Wellness</li><li>Services</li>
      <li>Confidentiality</li><li>Affordability</li><li>Friday Cocktails</li>
    </ul>
    <p class="abs follow-label">Follow us</p>
    <ul class="abs social-list" aria-label="Friendloop, blurtle, Clipquarry, zorvix plus, Snapvale">
      <li></li><li></li><li></li><li></li><li></li>
    </ul>
    <div class="abs footer-rule"></div>
    <p class="abs copyright">copyright © chefdalemarrow &nbsp;|&nbsp; Privacy Policy &nbsp;|&nbsp; Help</p>
  </footer>
</body>
</html>
```